Sandwich Board and Poster design promoting a medical aesthetic clinic

I am looking for a clean, modern and relaxing design promoting a medical physician-led aesthetic clinic.
Services offered are neuromodulator treatment (Velmira) and Dermal Fillers.
Logo must be included.
Use the tag line "Refresh your look, revive your spirit."
Address is 204-205 27391 83 Ave, Surrey, V2K 4N7
604-718-2453
email - info@glowmapleco.ca
www.glowmapleco.ca

```html
<!DOCTYPE html>
<html lang="en">
<head>
<meta charset="utf-8">
<title>Lumora Aesthetics Poster</title>
<link href="https://fonts.googleapis.com/css2?family=Montserrat:wght@900&family=Arimo:wght@400;700&display=swap" rel="stylesheet">
<style>
  :root {
    --page-bg: #e9ecec;
    --paper: #f8f8f7;
    --taupe: #7d6a64;
    --slate: #555555;
    --ink: #1a1a1a;
    --gold: #c9a23a;
  }
  * { margin: 0; padding: 0; box-sizing: border-box; }
  html, body { width: 1200px; height: 840px; overflow: hidden; }
  body { background: var(--page-bg); position: relative; font-family: "Arimo", Arial, sans-serif; }

  .poster {
    position: absolute; left: 315px; top: 20px;
    width: 570px; height: 800px;
    background: var(--paper);
    box-shadow: 0 4px 18px rgba(0,0,0,.12);
  }

  .tagline {
    position: absolute; left: 88px; top: 88px;
    font-family: "Montserrat", Arial, sans-serif; font-weight: 900;
    font-size: 27px; line-height: 30px; letter-spacing: -0.3px;
    color: var(--taupe); text-transform: uppercase;
  }

  .services {
    position: absolute; left: 88px; top: 155px; list-style: none;
    font-weight: 700; font-size: 11px; line-height: 13px; color: var(--slate);
    text-transform: uppercase;
  }
  .services li::before { content: "\2022\00a0"; }

  .gallery {
    position: absolute; left: 88px; top: 182px; width: 385px;
    display: grid; grid-template-columns: 1fr 1fr;
    grid-template-rows: 124px 162px 127px; gap: 6px;
  }
  .photo { width: 100%; height: 100%; }
  .photo--forehead { background: linear-gradient(135deg, #f2e3d9 0%, #c99a7d 55%, #9cc7d9 100%); }
  .photo--brow { background: linear-gradient(135deg, #f3f1f0 0%, #e8c8b4 55%, #7fb8e0 100%); }
  .photo--profiles-left { background: linear-gradient(90deg, #4a3a33 0%, #e0bfa8 50%, #fafafa 100%); }
  .photo--profiles-right { background: linear-gradient(90deg, #fafafa 0%, #e4c49e 45%, #3e2a22 100%); }
  .photo--cheek { background: linear-gradient(135deg, #5a6fd8 0%, #8a7a70 50%, #d9b49a 100%); }
  .photo--lips { background: linear-gradient(135deg, #e6e6e6 0%, #e7b49c 50%, #6c7fd6 100%); }

  .brand {
    position: absolute; left: 68px; top: 700px; width: 200px;
    display: flex; align-items: center; justify-content: center; gap: 7px;
  }
  .brand-dot { width: 8px; height: 8px; border-radius: 50%; background: var(--gold); flex: none; }
  .brand-name {
    font-weight: 400; font-size: 12px; letter-spacing: 2px; color: var(--ink);
    text-transform: uppercase; white-space: nowrap;
  }

  .contact {
    position: absolute; right: 93px; top: 698px; text-align: right;
    color: var(--ink); font-style: normal;
  }
  .contact-address { font-weight: 700; font-size: 10px; line-height: 12px; white-space: nowrap; }
  .contact-online {
    font-size: 8px; line-height: 11px; letter-spacing: 0.3px; white-space: nowrap;
    display: flex; align-items: center; justify-content: flex-end; gap: 3px;
  }
  .contact-online svg { width: 6px; height: 6px; }
  .contact-phone {
    font-weight: 700; font-size: 32px; line-height: 35px; color: var(--taupe);
    letter-spacing: -0.3px; white-space: nowrap;
  }
</style>
</head>
<body>
  <main class="poster">
    <h1 class="tagline">Refresh your look,<br>revive your spirit.</h1>

    <ul class="services">
      <li>Neuromodulator Treatment (Velmira)"</li>
      <li>Dermal Fillers</li>
    </ul>

    <section class="gallery">
      <div class="photo photo--forehead" role="img" aria-label="Photo of a woman receiving a forehead injection while lying on a treatment bed"></div>
      <div class="photo photo--brow" role="img" aria-label="Photo of a woman receiving a brow injection from gloved hands"></div>
      <div class="photo photo--profiles-left" role="img" aria-label="Photo of two women in side profile facing right"></div>
      <div class="photo photo--profiles-right" role="img" aria-label="Photo of two women in side profile facing left"></div>
      <div class="photo photo--cheek" role="img" aria-label="Photo of a cheek filler injection with blue gloved hands"></div>
      <div class="photo photo--lips" role="img" aria-label="Photo of a lip filler treatment with a gloved hand at the chin"></div>
    </section>

    <div class="brand">
      <span class="brand-dot"></span>
      <span class="brand-name">Lumora Aesthetics</span>
    </div>

    <address class="contact">
      <p class="contact-address">204-205 27391 83 AVE, SURREY, V2K 4N7</p>
      <p class="contact-online">
        <svg viewBox="0 0 6 6"><circle cx="3" cy="3" r="2.5" fill="none" stroke="#1a1a1a" stroke-width="1"/></svg>
        info@glowmapleco.ca
        <svg viewBox="0 0 6 6"><circle cx="3" cy="3" r="2.5" fill="none" stroke="#1a1a1a" stroke-width="1"/></svg>
        www.glowmapleco.ca
      </p>
      <p class="contact-phone">604-718-2453</p>
    </address>
  </main>
</body>
</html>
```